Powerpoint Template Design using new logo

I am a consultant for the biotech and pharmaceutical industry. I need a simple but effective powerpoint template that I can use for my company deliverables. I would like the design of the powerpoint template to incorporate the symbol used in our logo (attached). The dominant colors should complement the logo as well.
Please use the standard powerpoint slide size - not the new widescreen format.

Target Market(s)

Pharmaceutical and biotech companies

Industry/Entity Type

Pharmaceutical

Font styles to use
Serif
Sans Serif

Requirements
Must have
• Must include logo (attached). Colors must complement logo.
I'd prefer a white background for the slides. Design should provide as much space as possible. I'd also like to have a place for a slide title at the top with a "takeaway" or "summary" box underneath. Then as much area as possible for me to provide project results.

```html
<!DOCTYPE html>
<html lang="en">
<head>
<meta charset="utf-8">
<title>Project Slide Template</title>
<link rel="stylesheet" href="https://fonts.googleapis.com/css2?family=Ubuntu:wght@400;500;700&display=swap">
<style>
  :root {
    --brand-blue: #1467b0;
    --band-grey: #bcbdbf;
    --text-grey: #454545;
    --ink-dark: #333333;
    --paper: #ffffff;
  }
  * { margin: 0; padding: 0; box-sizing: border-box; }
  html, body {
    width: 1200px;
    height: 900px;
    overflow: hidden;
    background: var(--paper);
  }
  .slide {
    position: relative;
    width: 1200px;
    height: 900px;
    background: var(--paper);
    font-family: "Ubuntu", sans-serif;
    overflow: hidden;
  }
  .slide-header {
    position: absolute;
    top: 0; left: 0;
    width: 1200px;
    height: 84px;
  }
  .project-title {
    position: absolute;
    left: 21px;
    top: 14px;
    font-size: 43px;
    font-weight: 700;
    color: var(--brand-blue);
    letter-spacing: 0.3px;
  }
  .brand {
    position: absolute;
    left: 802px;
    top: 10px;
    display: flex;
    align-items: center;
    gap: 14px;
  }
  .brand-name {
    font-size: 50px;
    font-weight: 700;
    color: var(--brand-blue);
    letter-spacing: 1px;
  }
  .brand-mark {
    width: 14px;
    height: 14px;
    border-radius: 50%;
    background: var(--brand-blue);
  }
  .header-rule {
    position: absolute;
    left: 0;
    width: 1200px;
    background: var(--brand-blue);
  }
  .header-rule.primary { top: 76px; height: 2px; }
  .header-rule.secondary { top: 81px; height: 1px; }

  .content {
    position: absolute;
    left: 51px;
    top: 132px;
  }
  .section-heading {
    font-size: 42px;
    font-weight: 500;
    color: var(--brand-blue);
    margin-bottom: 28px;
  }
  .bullet-list { list-style: none; }
  .bullet-list li {
    position: relative;
    padding-left: 46px;
    height: 75px;
    font-size: 27px;
    font-weight: 500;
    color: var(--text-grey);
    line-height: 36px;
  }
  .bullet-list li::before {
    content: "";
    position: absolute;
    left: 6px;
    top: 8px;
    width: 21px;
    height: 21px;
    border-radius: 50%;
    background: var(--brand-blue);
  }

  .slide-footer {
    position: absolute;
    left: 0;
    bottom: 0;
    width: 1200px;
    height: 92px;
  }
  .slide-footer svg { position: absolute; left: 0; top: 0; }
  .copyright {
    position: absolute;
    left: 21px;
    top: 42px;
    font-size: 21px;
    color: var(--paper);
  }
  .page-number {
    position: absolute;
    right: 27px;
    top: 42px;
    font-size: 21px;
    color: var(--ink-dark);
  }
</style>
</head>
<body>
<div class="slide">
  <header class="slide-header">
    <h1 class="project-title">PROJECT TITLE HERE</h1>
    <div class="brand">
      <span class="brand-name">NOVARA</span>
      <span class="brand-mark"></span>
    </div>
    <div class="header-rule primary"></div>
    <div class="header-rule secondary"></div>
  </header>

  <main class="content">
    <h2 class="section-heading">Bullet Point Text</h2>
    <ul class="bullet-list">
      <li>Subtext here Subtext here Subtext here Subtext here</li>
      <li>Subtext here Subtext here Subtext here Subtext here</li>
      <li>Subtext here Subtext here Subtext here Subtext here</li>
      <li>Subtext here Subtext here Subtext here Subtext here</li>
      <li>Subtext here Subtext here Subtext here Subtext here</li>
      <li>Subtext here Subtext here Subtext here Subtext here</li>
      <li>Subtext here Subtext here Subtext here Subtext here</li>
    </ul>
  </main>

  <footer class="slide-footer">
    <svg width="1200" height="92" viewBox="0 0 1200 92" aria-hidden="true">
      <rect class="footer-band" x="0" y="0" width="1200" height="92" fill="var(--band-grey)"/>
      <polygon class="footer-divider" points="896,16 912,16 945,92 929,92" fill="var(--paper)"/>
      <polygon class="footer-panel" points="0,16 900,16 933,92 0,92" fill="var(--brand-blue)"/>
    </svg>
    <span class="copyright">Copyrighttext here</span>
    <span class="page-number">01</span>
  </footer>
</div>
</body>
</html>
```